Baby and Kids e-shop (Russian language is needed)

We need a web design for e-shop of a Russian company based in Moscow. We sell maternity things, baby and kids goods, clothes, toys, furniture, home and decor, etc.
We need the design that will suit to the exhisting logo. It should be simple and comfortable to the consumers. Attractive but not too bright (so that the goods' pictures attract more attention to them instead of the design).
The domain name of the company is quillbeck.ru
Design of the main page should be similar to the idea of lulloday.com All button names of the main page are provided in attached file.
While choosing certain category from the menu, we should see the list of goods to the left and list of brands to the right (example: http://www.krovatka-dom.ru/?welcome).

We need:
- main page
- page of the catalogue
- page of the certain category from the catalogue
- page with a certain good
- cart page
- payment page
- quill beck club page (banner and text)
- registration page (banner, registration form, text)
Updates

Target Market(s)

pregnant women, young moms

Industry/Entity Type

Baby

Requirements
Must have
• The webdesign should be very clear and similar to lulloday.com You can suggest a kind of design similar to kindrelo.de, tappelo.de.
The web design should clear state that it is targeted on kids goods, but it is a family e-shop as well.
Nice to have
• 1) In general the design shall be the same as provided sample we like. The design of a page with a concrete good should have tabs: 1) about this good, 2) payment, 3) delivery and return, 4) review; like this: http://www.harbordressco.com/t-shirts-c4/vornik-classic-h-tee-ridge-t-shirt-p81174
2) we need design of stickers like in shown example above: 5% off (First order) and Free Coupon for X Rubles for every 1000 Rubles spent online
3) instead of Bookmark&share, ask a question, e-mail a friend and add to wish list, we should have "share" (Chatterly, Druzhnet, Svoyakh - short logos, I will send examples), "ask a question", "e-mail a friend" and "add to gift list" (All this information is contained in downloaded files).

```html
<!DOCTYPE html>
<html lang="en">
<head>
<meta charset="utf-8">
<title>Quill Beck — baby and family store</title>
<link href="https://fonts.googleapis.com/css2?family=Arimo:ital,wght@0,400;0,700;1,700&family=PT+Serif:ital,wght@1,700&display=swap" rel="stylesheet">
<style>
:root{
  --red:#c8141c;
  --red-dark:#8e0b10;
  --red-deep:#6f080c;
  --pink:#e8336b;
  --green:#9cc13a;
  --yellow:#f7c21a;
  --orange:#f39a12;
  --grey:#eeeeee;
  --grey-mid:#cfcfcf;
  --text:#333;
  --white:#fff;
}
*{box-sizing:border-box;margin:0;padding:0}
html,body{width:719px;height:1200px;overflow:hidden}
body{font-family:"Arimo",Arial,sans-serif;font-size:10px;color:var(--text);background:var(--white)}
.page{position:relative;width:719px;height:1200px;background:var(--grey)}
.abs{position:absolute}

.topbar{left:0;top:0;width:719px;height:20px;background:var(--white);display:flex;justify-content:space-between;align-items:center;padding:0 10px;font-size:9px}
.topbar nav a{margin-left:8px;color:var(--text);text-decoration:none}
.topbar .login{color:var(--red)}

.header{left:0;top:20px;width:719px;height:105px;background:linear-gradient(var(--red),var(--red-dark))}
.logo{left:14px;top:8px;width:120px;height:90px;display:flex;align-items:center;gap:6px}
.logo .dot{width:16px;height:16px;border-radius:50%;background:var(--yellow)}
.logo span{color:var(--white);font-weight:700;font-size:17px}
.mainnav{left:150px;top:0;display:flex}
.mainnav a{display:flex;align-items:center;justify-content:center;text-align:center;width:82px;height:42px;color:var(--white);font-size:10px;font-weight:700;text-decoration:none;border-left:1px solid rgba(255,255,255,.3);line-height:1.15}
.mainnav a.active{background:var(--white);color:var(--red);border-radius:0 0 4px 4px}
.searchrow{left:150px;top:52px;display:flex;gap:10px;align-items:center}
.field{display:flex}
.field input{width:120px;height:18px;border:0;border-radius:2px 0 0 2px}
.field button{height:18px;padding:0 10px;border:0;background:var(--pink);color:var(--white);font:700 9px "Arimo",sans-serif}
.city{width:110px;height:18px;background:var(--white);border-radius:2px;padding:3px 6px;font-size:9px;font-weight:700}

.banner{left:10px;top:138px;width:496px;height:268px;background:var(--white);border:1px solid var(--grey-mid);border-radius:6px}
.screen{left:32px;top:16px;width:430px;height:232px;border:8px solid #ddd;border-radius:8px;background:linear-gradient(#f5f5f5,#e6e6e6);overflow:hidden}
.photo{left:0;top:0;width:170px;height:216px;background:radial-gradient(circle at 50% 35%,#f7d24a,#e07a3a 55%,#c8434a)}
.slide-text{left:232px;top:60px;width:210px}
.slide-text h2{font:italic 700 20px "PT Serif",Georgia,serif;color:#2b2b2b;margin-bottom:8px}
.slide-text p{font-size:10px;line-height:1.35;color:#555}
.arrow{top:122px;width:18px;height:18px;border-radius:50%;background:#bbb}
.dots{left:226px;top:252px;display:flex;gap:5px}
.dots i{width:6px;height:6px;border-radius:50%;background:#ccc}
.dots i.on{background:var(--red)}

.basket{left:516px;top:138px;width:194px;height:112px;background:var(--yellow);border-radius:6px;padding:10px}
.basket h3{font:italic 700 18px "PT Serif",Georgia,serif;color:var(--red);margin:0 0 8px 40px}
.basket .row{display:flex;justify-content:space-between;font-size:9px;margin-bottom:5px}
.basket select,.filters select,.toolbar select{font:9px "Arimo",sans-serif;height:15px;border:1px solid #bbb}

.filters{left:516px;top:258px;width:194px;height:148px;background:var(--pink);border-radius:6px;padding:10px 8px}
.filters .f{display:flex;justify-content:space-between;align-items:center;color:var(--white);font-weight:700;font-size:9px;height:22px;line-height:1.05}
.filters select{width:96px}
.filters button{margin:6px 0 0 60px;background:var(--red);color:var(--white);border:0;border-radius:3px;font:700 9px "Arimo",sans-serif;padding:4px 10px}

.toolbar{left:10px;top:416px;width:496px;height:26px;background:var(--white);border-bottom:2px solid var(--red);display:flex;align-items:center}
.toolbar h3{height:26px;width:110px;background:var(--red);color:var(--white);font:italic 700 13px "PT Serif",Georgia,serif;display:flex;align-items:center;padding-left:10px;border-radius:4px 0 0 0}
.toolbar label{font-size:8px;margin-left:20px;width:90px;line-height:1.05}
.grid{left:10px;top:452px;width:496px;display:grid;grid-template-columns:repeat(3,156px);gap:14px 14px}
.card{background:var(--white);border:1px solid var(--grey-mid);border-radius:4px;height:196px;padding:8px;text-align:center}
.card .pic{height:84px;border:1px solid #eee;border-radius:3px}
.pic.toy{background:radial-gradient(circle at 50% 60%,#d62b2b,#f3f3f3 70%)}
.pic.shoe{background:radial-gradient(ellipse at 50% 60%,#6e4a3a,#f3f3f3 65%)}
.pic.dress{background:radial-gradient(ellipse at 50% 50%,#a8c6d8,#f3f3f3 65%)}
.card .name{color:var(--red);font-size:8px;font-weight:700;margin:8px 0 4px;white-space:nowrap}
.card .price{font-size:24px;font-weight:700;color:#333}
.stars{display:flex;justify-content:center;gap:2px;margin:3px 0 6px}
.stars i{width:8px;height:8px;background:#ccc;clip-path:polygon(50% 0,61% 35%,98% 35%,68% 57%,79% 91%,50% 70%,21% 91%,32% 57%,2% 35%,39% 35%)}
.stars i.on{background:var(--orange)}
.card button{background:var(--red);color:var(--white);border:0;border-radius:3px;font:700 10px "Arimo",sans-serif;padding:5px 14px}

.cats{left:516px;top:416px;width:194px;height:412px;background:var(--green);border-radius:6px;padding:16px 12px;list-style:none}
.cats li{color:var(--white);font-size:10px;height:22.4px;display:flex;align-items:center;gap:6px}
.cats li::before{content:"";width:4px;height:4px;border-radius:50%;background:var(--white)}

.social{left:516px;top:838px;width:194px}
.social p{font:italic 700 10px "PT Serif",Georgia,serif;margin-bottom:6px}
.social .icons{display:flex;gap:6px}
.social .icons i{width:22px;height:22px;border-radius:4px;background:#4a66a8}
.social .icons i:nth-child(2){background:#3aa7e0}
.social .icons i:nth-child(3){background:#e86a1c}
.social .icons i:nth-child(4){background:#5b7fa6}
.social .icons i:nth-child(5){background:#d33}

.partners{left:10px;top:918px;width:700px;height:44px;background:var(--white);border-radius:4px;display:flex;justify-content:space-around;align-items:center}
.partners i{width:60px;height:22px;border-radius:4px;background:#d9d9d9}
.partners i:nth-child(odd){background:#e7c9d2}

.news{left:10px;top:968px;width:700px;height:38px;background:var(--white);border-radius:4px;display:flex;align-items:center;gap:14px;padding:0 10px}
.news h3{font:italic 700 13px "PT Serif",Georgia,serif;width:90px}
.news time{color:var(--red);font-size:8px;font-weight:700}
.news p{font-size:8px;line-height:1.2;width:470px}

.footer{left:0;top:1014px;width:719px;height:186px;background:linear-gradient(var(--red),var(--red-deep));color:var(--white)}
.footer h4{font:italic 700 14px "PT Serif",Georgia,serif;margin-bottom:10px}
.col{position:absolute;top:14px;font-size:9px;line-height:1.9}
.col ul{list-style:none}
.col li::before{content:"\25B8 ";color:var(--yellow)}
.cards{display:flex;gap:5px;width:170px}
.cards i{width:34px;height:22px;border-radius:3px;background:var(--white)}
.copy{font-size:8px;line-height:1.35;margin-top:8px;width:170px}
</style>
</head>
<body>
<div class="page">

  <div class="abs topbar">
    <span>welcome msg!</span>
    <nav><a>My Account</a><a>My Wishlist</a><a>My Cart</a><a>Checkout</a><a class="login">Log in</a></nav>
  </div>

  <header class="abs header">
    <div class="abs logo"><span class="dot"></span><span>Quill Beck</span></div>
    <nav class="abs mainnav">
      <a class="active">About Us</a><a>Shipping and Payments</a><a>Contact us</a><a>Share of the week</a><a>Wholesaler</a><a>Familystore</a>
    </nav>
    <div class="abs searchrow">
      <div class="field"><input aria-label="search"><button>Search</button></div>
      <div class="field"><input aria-label="subscribe"><button>Subscribe</button></div>
      <div class="city">Your City ▾</div>
    </div>
  </header>

  <section class="abs banner">
    <div class="abs screen">
      <div class="abs photo" role="img" aria-label="Girl holding a sunflower"></div>
    </div>
    <div class="abs slide-text">
      <h2>Lorem Ipsum</h2>
      <p>Lorem Ipsum is simply dummy text of the printing and typesetting industry. It is a long established fact that a reader will be distracted by the readable content of a page when looking at its layout.</p>
    </div>
    <span class="abs arrow" style="left:8px"></span>
    <span class="abs arrow" style="right:8px"></span>
    <div class="abs dots"><i class="on"></i><i></i><i></i><i></i></div>
  </section>

  <aside class="abs basket">
    <h3>Basket</h3>
    <div class="row"><span>BASKET% your basket</span></div>
    <div class="row"><span>24 products</span><span>16 all</span></div>
    <div class="row"><span>Currency</span><select><option>RUB</option></select></div>
  </aside>

  <aside class="abs filters">
    <div class="f">Shoes<select><option>All brands</option></select></div>
    <div class="f">Children's wear<select><option>All brands</option></select></div>
    <div class="f">Clothes for Moms<select><option>All brands</option></select></div>
    <div class="f">Fancy clothe<select><option>All brands</option></select></div>
    <div class="f">Everything for baby<select><option>All brands</option></select></div>
    <button>Selection</button>
  </aside>

  <div class="abs toolbar">
    <h3>Our Products</h3>
    <label>No. of products to display</label><select><option>12</option></select>
    <label>Show products</label><select><option>All</option></select>
  </div>

  <section class="abs grid">
    <article class="card"><div class="pic toy" role="img" aria-label="Red ride-on toy"></div><p class="name">Brightwell Roll-Along Red Dragon</p><p class="price">$25.85</p><div class="stars"><i class="on"></i><i class="on"></i><i class="on"></i><i></i><i></i></div><button>Add to cart</button></article>
    <article class="card"><div class="pic shoe" role="img" aria-label="Brown children's shoes"></div><p class="name">Brightwell Roll-Along Red Dragon</p><p class="price">$25.85</p><div class="stars"><i class="on"></i><i class="on"></i><i class="on"></i><i></i><i></i></div><button>Add to cart</button></article>
    <article class="card"><div class="pic dress" role="img" aria-label="Girl's printed summer dress"></div><p class="name">Brightwell Roll-Along Red Dragon</p><p class="price">$25.85</p><div class="stars"><i class="on"></i><i class="on"></i><i class="on"></i><i></i><i></i></div><button>Add to cart</button></article>
    <article class="card"><div class="pic toy" role="img" aria-label="Red ride-on toy"></div><p class="name">Brightwell Roll-Along Red Dragon</p><p class="price">$25.85</p><div class="stars"><i class="on"></i><i class="on"></i><i class="on"></i><i></i><i></i></div><button>Add to cart</button></article>
    <article class="card"><div class="pic shoe" role="img" aria-label="Brown children's shoes"></div><p class="name">Brightwell Roll-Along Red Dragon</p><p class="price">$25.85</p><div class="stars"><i class="on"></i><i class="on"></i><i class="on"></i><i></i><i></i></div><button>Add to cart</button></article>
    <article class="card"><div class="pic dress" role="img" aria-label="Girl's printed summer dress"></div><p class="name">Brightwell Roll-Along Red Dragon</p><p class="price">$25.85</p><div class="stars"><i class="on"></i><i class="on"></i><i class="on"></i><i></i><i></i></div><button>Add to cart</button></article>
  </section>

  <ul class="abs cats">
    <li>Sales of the week</li><li>Holidays and Gifts</li><li>Toys</li><li>Girls</li><li>Boys</li><li>Baby</li><li>Mittens, gloves</li><li>Children's Shoes</li><li>Hats</li><li>School Uniform</li><li>For expectant mothers</li><li>Carnival costumes</li><li>Winter Games</li><li>Everything for baby</li><li>Textile accessories</li><li>Mother and baby health</li><li>Furniture and car seats</li>
  </ul>

  <div class="abs social">
    <p>Place with your friends</p>
    <div class="icons"><i></i><i></i><i></i><i></i><i></i></div>
  </div>

  <div class="abs partners"><i></i><i></i><i></i><i></i><i></i><i></i><i></i><i></i></div>

  <div class="abs news">
    <h3>Latest news</h3>
    <time>01/12/2011</time>
    <p>Criteria for selection of prenatal. Choosing a beautiful and comfortable clothes, do not forget about the underwear, in particular, on the bra. During pregnancy, breasts become more sensitive, changes in volume.</p>
  </div>

  <footer class="abs footer">
    <div class="col" style="left:16px;width:190px">
      <h4>Contact</h4>
      <p>+7 (495) 000-12-34 (Moscow)</p>
      <p>info@quillbeck.ru</p>
    </div>
    <div class="col" style="left:220px;top:42px"><ul><li>Site Map</li><li>Search Terms</li><li>Advanced Search</li></ul></div>
    <div class="col" style="left:360px;top:42px"><ul><li>Check Order Status</li><li>Returns &amp; Exchanges</li><li>Shipping Options &amp; Charges</li><li>Product Recall</li></ul></div>
    <div class="col" style="left:530px">
      <h4>Payments</h4>
      <div class="cards"><i></i><i></i><i></i><i></i></div>
      <p class="copy">© quillbeck.ru online store goods for children and expectant mothers 2010 All rights reserved</p>
    </div>
  </footer>

</div>
</body>
</html>
```